Regional Showdown Flyer for Holiday Program

Need a one page flyer, can be back to front or one page, ensuring you can fit all information, colourful, aimed at a market of 8-13 year old boys and girls.
The flyer needs to be noticed, needs to have certain information on it and needs to be Autralian Rule Football orientated.
Have uploaded file so you can understand the style (not content), style of flyer I am looking at getting submitted.

Target Market(s)

8-13 year old boys and girls and their parents.

Requirements
Must have
• Regional Showdown Event
• Price for Regional Showdown Day will be $85
• Strictly Limited Places, only the best footballers should enter this challenge
• Inaugural event, be the first Regional Showdown Winner for your age!
• Do you love a challenge! Put yourself to the test!
• Are you up to it - Water Slide Goal Kicking Contest! The fastest kick in the West (tested by our very own speed gun)! Can you survive the Footy Titan Trail or Last One Standing Goal Kicking! These challenges are crazy are super fun!
• If you think you can deliver on the big stage then this is for YOU!
• All District age winners will receive prizes, awards and the adulation from all their peers!
• Year's 3-5 from 9am to 12pm
• Year's 6-8 from 1-4pm
• All challengers compete against their own age
• Lunch Provided
• Monday 16th April - Upper Tarrowby Regional Showdown Day at Tarrowby Oval
• Tuesday 17th April - North Tarrowby Regional Showdown Day at Kilmorna Reserve
• Wednesday 18th April - Yarlo Regional Showdown Day - Dunhaven Football Club
• Every Challenge Participant receives a District Football!
• Need to put all 3 District Football Logos on the bottom of the flyer, logos attached at bottom.
Nice to have
• Plenty of colour, if you can fit all information on one page that would be fine
Should not have
• Dull, boring, any footballs should be Aussie Rules footballs not NFL or soccer

```html
<!DOCTYPE html>
<html lang="en">
<head>
<meta charset="utf-8">
<title>Regional Showdown Event Flyer</title>
<link rel="stylesheet" href="https://fonts.googleapis.com/css2?family=Alfa+Slab+One&family=Dosis:wght@500;600;700&family=Signika:wght@400;600&display=swap">
<style>
:root{
  --teal:#127081;
  --maroon:#7a1a14;
  --purple:#6a48a8;
  --white:#ffffff;
  --brown:#6e3a1e;
  --pale:#d9ece6;
  --prize-green:#3aa63c;
}
*{margin:0;padding:0;box-sizing:border-box}
html,body{width:883px;height:1200px;overflow:hidden;background:#fff}
.flyer{position:relative;width:883px;height:1200px;overflow:hidden;
  background:linear-gradient(180deg,#1fa23f 0%,#5cbc3a 14%,#b7d92f 32%,#e6ea3a 42%,#cfe9b8 55%,#bfe6f2 68%,#a9dcec 82%,#1d98b4 100%);
  font-family:"Signika",sans-serif}
.crowd{position:absolute;left:0;bottom:0;width:883px;height:230px;
  background:linear-gradient(180deg,rgba(22,140,170,0) 0%,rgba(22,140,170,.45) 45%,rgba(10,110,140,.8) 100%)}
.abs{position:absolute}
.title{font-family:"Alfa Slab One",serif;color:#eef6e6;letter-spacing:1px;white-space:nowrap;text-shadow:0 2px 0 rgba(0,0,0,.12)}
.title-main{left:0;top:40px;width:883px;text-align:center;font-size:54px;line-height:64px}
.title-sub{left:322px;top:100px;font-size:56px;line-height:64px}
.price{left:160px;top:110px;width:122px;height:117px;border-radius:50%;background:var(--brown);
  border:2px dashed var(--white);color:var(--white);font-family:"Dosis",sans-serif;font-weight:700;font-size:42px;
  display:flex;align-items:center;justify-content:center}
.day{left:300px;top:162px;font-family:"Dosis",sans-serif;font-weight:600;font-size:37px;line-height:46px;color:var(--white);letter-spacing:1.5px;white-space:nowrap}
.ball{left:556px;top:88px;width:284px;height:327px}
.intro{left:53px;top:236px;width:620px;color:var(--white);font-weight:600;font-size:28px;line-height:31.5px;letter-spacing:.3px;
  text-shadow:1px 1px 2px rgba(0,0,0,.35);white-space:nowrap}
.head{font-family:"Dosis",sans-serif;font-weight:600;color:var(--maroon);white-space:nowrap;line-height:1}
.head-love{left:53px;top:402px;font-size:50px}
.tagline{left:54px;top:449px;font-family:"Dosis",sans-serif;font-weight:500;font-size:21px;line-height:24px;color:var(--purple)}
.head-up{left:53px;top:472px;font-size:51px}
.lunch{left:626px;top:388px;width:208px;height:146px;border-radius:50%;background:var(--teal);border:2px dashed var(--white);
  color:#e8f3f1;font-family:"Alfa Slab One",serif;font-size:22px;line-height:34px;text-align:center;
  display:flex;align-items:center;justify-content:center}
.events{left:55px;top:517px;width:800px;font-family:"Dosis",sans-serif;font-weight:500;font-size:25px;line-height:29px;color:var(--purple)}
.events strong{color:var(--maroon);font-weight:700}
.you-line{left:55px;top:626px;font-family:"Dosis",sans-serif;font-weight:500;font-size:25px;line-height:40px;color:var(--purple);white-space:nowrap}
.you-line .you{font-weight:700;font-size:48px;color:var(--maroon);margin-left:6px;vertical-align:-4px}
.prizes{left:0;top:671px;width:883px;text-align:center;font-family:"Dosis",sans-serif;font-weight:700;font-size:26px;line-height:30px;color:var(--prize-green)}
.session{top:741px;height:39px;background:var(--teal);color:var(--white);font-family:"Dosis",sans-serif;font-weight:600;font-size:25px;
  display:flex;align-items:center;justify-content:center;letter-spacing:.5px;white-space:nowrap}
.session-junior{left:58px;width:362px}
.session-senior{left:462px;width:362px}
.divider{left:439px;top:747px;width:3px;height:27px;background:var(--teal)}
.age-note{left:0;top:785px;width:883px;text-align:center;font-family:"Dosis",sans-serif;font-weight:600;font-size:24px;line-height:28px;color:var(--maroon)}
.dates{left:53px;top:821px;width:800px;font-family:"Dosis",sans-serif;line-height:27.5px;white-space:nowrap}
.date{font-weight:700;font-size:25px;color:var(--maroon)}
.date sup{font-size:13px}
.venue{font-weight:500;font-size:26px;color:var(--purple)}
.bonus{left:53px;top:1000px;font-family:"Dosis",sans-serif;font-weight:700;font-size:27px;line-height:30px;color:var(--maroon);white-space:nowrap}
.club{top:1043px;width:206px;height:130px;border-radius:50%;background:var(--pale);border:2px dashed var(--teal);
  display:flex;align-items:center;justify-content:center;gap:8px;font-family:"Dosis",sans-serif;font-weight:700;font-size:19px;color:var(--teal);text-align:center;line-height:22px}
.club .dot{width:14px;height:14px;border-radius:50%;background:var(--teal);flex:none}
.club-a{left:42px}.club-b{left:336px}.club-c{left:628px}
</style>
</head>
<body>
<main class="flyer">
  <div class="crowd abs" role="img" aria-label="Faint silhouettes of cheering fans and a player taking a mark"></div>

  <h1 class="title title-main abs">REGIONAL SHOWDOWN</h1>
  <div class="title title-sub abs">EVENT</div>
  <div class="price abs">$85</div>
  <div class="day abs">CHALLENGE DAY</div>

  <svg class="ball abs" viewBox="0 0 284 327" role="img" aria-label="Illustration of a leather Australian Rules football with white laces">
    <defs>
      <radialGradient id="leather" cx="40%" cy="35%" r="70%">
        <stop offset="0" stop-color="#c2552a"/>
        <stop offset="0.7" stop-color="#9a3a1c"/>
        <stop offset="1" stop-color="#7a2a14"/>
      </radialGradient>
    </defs>
    <ellipse cx="142" cy="163" rx="100" ry="170" transform="rotate(35 142 163)" fill="url(#leather)"/>
  </svg>

  <p class="intro abs">Strictly Limited Places,<br>only the best footballers should<br>enter this challenge.<br>Inaugural event, be the first<br>Regional Showdown Winner for your age!</p>

  <h2 class="head head-love abs">DO YOU LOVE A CHALLENGE!</h2>
  <p class="tagline abs">Put yourself to the test!</p>
  <h2 class="head head-up abs">ARE YOU UP TO IT</h2>

  <div class="lunch abs">LUNCH<br>PROVIDED</div>

  <p class="events abs">Water Slide Goal Kicking Contest!<br>The fastest kick in the West (tested by our very own speed gun)! Can you<br>survive the <strong>Footy Titan Trail</strong> or <strong>Last One Standing Goal Kicking!</strong><br>These challenges are crazy, super fun!</p>
  <p class="you-line abs">If you think you can deliver on the big stage then this is for<span class="you">YOU!</span></p>

  <p class="prizes abs">ALL DISTRICT AGE WINNERS WILL RECEIVE PRIZES, AWARDS AND THE<br>ADULATION FROM ALL THEIR PEERS!</p>

  <div class="session session-junior abs">YEAR'S 3-5 FROM 9AM TO 12PM</div>
  <div class="divider abs"></div>
  <div class="session session-senior abs">YEAR'S 6-8 FROM 1PM TO 4PM</div>
  <p class="age-note abs">All challengers compete against their own age</p>

  <div class="dates abs">
    <div class="date">MONDAY 16<sup>TH</sup> APRIL</div>
    <div class="venue">Upper Tarrowby Regional Showdown Day at Tarrowby Oval</div>
    <div class="date">TUESDAY 17<sup>TH</sup> APRIL</div>
    <div class="venue">North Tarrowby Regional Showdown Day at Kilmorna Reserve</div>
    <div class="date">WEDNESDAY 18<sup>TH</sup> APRIL</div>
    <div class="venue">Yarlo Regional Showdown Day - Dunhaven Football Club</div>
  </div>

  <p class="bonus abs">EVERY CHALLENGE PARTICIPANT RECEIVES A DISTRICT FOOTBALL!</p>

  <div class="club club-a abs"><span class="dot"></span><span>IRONBARK<br>DISTRICT</span></div>
  <div class="club club-b abs"><span class="dot"></span><span>YARLO<br>DISTRICT</span></div>
  <div class="club club-c abs"><span class="dot"></span><span>COASTLINE<br>DISTRICT</span></div>
</main>
</body>
</html>
```